Website for Solar Renewable Company

We Driftwell Solar, are in need on a new website design. We design , manufacture and install floating solar plants. These plants are installed on reservoir , lakes and captive reservoir. We would like to build a professional website which shows the technical competency of our company as our product is highly technical .

Videos our projects
https://www.vidmora.example/watch?v=aQ3rT8LmZ2x
https://www.vidmora.example/watch?v=pB7nK2wXeR4&t=115s
https://www.vidmora.example/watch?v=mJ9_5QdTyHV&t=4s

Please see reference competitor websites
https://bormivane-plat.net/
https://en.tallmerenergy.com/
https://qx-hovrelt.com/

Tabs Needed
- About
- Team
- Solutions
- Projects
- News Update
- Contact

These are not certain - you can change the tabs if you want

Target Market(s)

Developer and EPC companies

Industry/Entity Type

Solar , Renewable Energy, Power

Coding

Coded - Design and coding required

Number of Pages Required

5+ page

Colors
0094D4
00A9DD
6FCCEA
C7EBF8
E9F6FB

Requirements
Nice to have
• Videos

```html
<!DOCTYPE html>
<html lang="en">
<head>
<meta charset="utf-8">
<title>Driftwell Solar — Floating Solar Plants</title>
<link href="https://fonts.googleapis.com/css2?family=Montserrat:wght@400;500;600;700;800&family=Krona+One&display=swap" rel="stylesheet">
<style>
:root{
  --navy:#23417f;
  --navy-dark:#1b3566;
  --orange:#f7a918;
  --blue:#0094D4;
  --blue-2:#00A9DD;
  --blue-3:#6FCCEA;
  --blue-4:#C7EBF8;
  --blue-5:#E9F6FB;
  --grey:#8c8c8c;
  --field:#dcdcdc;
  --ink:#1e2a44;
  --white:#fff;
}
*{box-sizing:border-box;margin:0;padding:0}
html,body{width:1200px;height:4983px;overflow:hidden}
body{position:relative;background:var(--white);font-family:"Montserrat",sans-serif;color:var(--ink)}
.abs{position:absolute}
.brand{font-family:"Montserrat",sans-serif;font-weight:800;color:var(--navy);display:flex;align-items:center;gap:8px}
.brand-dot{width:14px;height:14px;border-radius:50%;background:var(--orange)}
.nav{position:absolute;top:34px;right:36px;display:flex;gap:30px;font-size:16px;font-weight:500}
.hero-bg{left:0;top:88px;width:1200px;height:724px;background:linear-gradient(180deg,#b8c8da 0%,#cfd8df 55%,#9aa98a 100%)}
.hero-bg-low{left:0;top:812px;width:225px;height:78px;background:#8f9e80}
.display{font-family:"Krona One",sans-serif;text-align:center;width:1200px;left:0}
.hero-solar{top:180px;font-size:112px;color:var(--navy);letter-spacing:4px}
.hero-energy{top:282px;font-size:100px;color:transparent;-webkit-text-stroke:3px var(--navy);letter-spacing:4px}
.hero-title{top:400px;width:1200px;text-align:center;font-size:58px;font-weight:500;color:#111;line-height:66px}
.hero-copy{top:552px;left:300px;width:600px;text-align:center;font-size:20px;line-height:26px;color:#222}
.btn{position:absolute;display:flex;align-items:center;justify-content:center;font-size:32px;font-weight:500}
.btn-solutions{left:343px;top:645px;width:231px;height:50px;background:var(--orange);color:#111}
.btn-projects{left:625px;top:645px;width:233px;height:50px;background:var(--navy);color:#fff}
.stats-photo{left:225px;top:812px;width:235px;height:158px;background:linear-gradient(180deg,#8cb4de,#3c5f96 60%,#8b9a74)}
.stats{left:460px;top:812px;width:740px;height:158px;background:var(--navy);display:flex;color:#fff}
.stat{flex:1;display:flex;flex-direction:column;align-items:center;padding-top:8px}
.stat-num{font-size:44px;font-weight:700;color:var(--orange);line-height:46px;margin-top:6px}
.stat-label{font-size:21px;line-height:20px}
.about-photo{left:130px;top:1052px;width:418px;height:416px;background:linear-gradient(180deg,#5d9ad8 0%,#a9c9ea 50%,#7f99b2 100%)}
.about-badge{left:74px;top:1410px;width:118px;height:118px;background:var(--blue);color:#fff;text-align:center;padding-top:22px}
.about-badge b{font-size:34px;color:var(--orange);display:block;line-height:34px}
.about-badge span{font-size:13px;font-weight:600;line-height:16px;display:block}
.outline-title{font-family:"Krona One",sans-serif;color:transparent;-webkit-text-stroke:2px #9aa8c4;font-size:52px}
.about-title{left:603px;top:1048px}
.sub-blue{font-size:22px;font-weight:500;color:var(--navy)}
.about-list{left:608px;top:1148px;width:420px;font-size:13.5px;line-height:21.5px;list-style:none;color:#222}
.about-list li{position:relative;padding-left:25px}
.about-list li::before{content:"»";position:absolute;left:0;top:-3px;font-size:20px;color:var(--navy);font-weight:700}
.about-list li.sub{padding-left:55px}
.about-list li.sub::before{left:30px;color:var(--orange)}
.find-more{left:603px;top:1443px;width:173px;height:37px;background:var(--orange);display:flex;align-items:center;gap:8px;padding-left:10px;font-size:22px;font-weight:600;color:var(--navy)}
.partners{left:0;top:1670px;width:1200px;height:102px;background:var(--grey);display:flex;align-items:center;justify-content:space-around;padding:0 50px}
.partner{display:flex;align-items:center;gap:10px;color:#b7b7b7;font-size:34px;font-weight:500}
.partner i{width:56px;height:56px;border-radius:50%;border:4px solid #b7b7b7;display:block}
.team{left:0;top:1772px;width:1200px;height:480px;background:linear-gradient(180deg,#5a6d99 0%,#3a5286 100%)}
.team-title{top:1795px;width:1200px;text-align:center;font-family:"Krona One",sans-serif;font-size:40px;color:#fff;-webkit-text-stroke:1.5px #111;letter-spacing:2px}
.member{position:absolute;top:1865px;width:272px;height:350px;border:3px solid #fff;border-radius:136px;display:flex;flex-direction:column;align-items:center}
.member .portrait{width:200px;height:200px;border-radius:50%;margin-top:22px;border:3px solid var(--blue-2)}
.member .name{font-family:"Montserrat",sans-serif;font-size:27px;font-weight:800;color:var(--orange);margin-top:12px;white-space:nowrap;line-height:32px}
.member .role{font-size:21px;color:#fff;white-space:nowrap}
.est-photo{left:174px;top:2332px;width:484px;height:483px;border:3px solid var(--orange);background:linear-gradient(180deg,#cfd9e3 0%,#8ea6bd 25%,#3d5d92 60%,#2d4a85 100%)}
.est-photo h3{position:absolute;top:325px;width:100%;text-align:center;color:#fff;font-weight:500;font-size:54px;line-height:54px}
.est-photo h4{position:absolute;top:383px;width:100%;text-align:center;color:#fff;font-weight:500;font-size:36px}
.est-form{left:555px;top:2383px;width:475px;height:474px;border:4px solid var(--navy);background:#fff}
.est-title{left:676px;top:2404px;font-size:34px;font-weight:600;color:var(--navy);line-height:42px}
.field{position:absolute;left:665px;width:351px;height:36px;background:var(--field);font-size:21px;font-weight:500;padding-left:14px;display:flex;align-items:center;color:#222}
.calc{left:735px;top:2784px;width:210px;height:38px;background:var(--blue);color:#fff;font-size:21px;font-weight:600;display:flex;align-items:center;justify-content:center}
.facts-title{left:118px;top:2985px;-webkit-text-stroke:2px var(--orange);font-size:46px}
.facts-sub{left:120px;top:3055px;font-size:29px;font-weight:600;color:var(--navy);line-height:34px;letter-spacing:1px}
.facts-copy{left:118px;top:3138px;width:385px;font-size:18.5px;line-height:21.5px;color:#222}
.map{left:650px;top:2950px;width:520px;height:490px;background:radial-gradient(ellipse at 45% 50%,#f3f3f3 0%,#e6e6e6 60%,#fff 75%)}
.map-label{position:absolute;font-size:21px;color:#fff;-webkit-text-stroke:1px #222;text-align:center;line-height:24px}
.work-bg{left:0;top:3465px;width:1200px;height:625px;background:linear-gradient(180deg,var(--blue-5),#eaf3fa)}
.work-ghost{top:3490px;font-size:68px;color:transparent;-webkit-text-stroke:2px #c9cfdb}
.work-title{top:3545px;width:1200px;text-align:center;font-size:46px;font-weight:700;color:var(--navy);letter-spacing:2px}
.work-copy{top:3597px;left:180px;width:840px;text-align:center;font-size:15px;line-height:17px;color:#222}
.proj{position:absolute;top:3655px;width:205px;height:310px}
.query{left:258px;top:4013px;width:686px;height:82px;background:var(--navy)}
.query-photo{left:258px;top:4013px;width:172px;height:82px;background:linear-gradient(180deg,#6e86b0,#40598b)}
.query-label{left:258px;top:4019px;width:172px;text-align:center;font-family:"Krona One",sans-serif;font-size:18px;line-height:34px;color:#fff;-webkit-text-stroke:1px #111;white-space:nowrap}
.qfield{position:absolute;top:4043px;height:24px;background:#fff;font-size:17px;font-weight:500;padding-left:6px;color:#222}
.send{left:853px;top:4043px;width:82px;height:24px;background:var(--orange);color:#fff;font-size:17px;font-weight:700;display:flex;align-items:center;justify-content:center;letter-spacing:2px}
.blogs-ghost{left:140px;top:4195px;font-size:52px;-webkit-text-stroke:2px #b9c0d2}
.blogs-title{left:140px;top:4195px;font-size:40px;font-weight:500;color:var(--navy);letter-spacing:2px}
.plus{left:939px;top:4172px;width:92px;height:92px;border-radius:50%;background:var(--orange)}
.card{position:absolute;top:4292px;width:273px;height:343px;background:var(--navy)}
.card .img{height:170px}
.card .date{font-size:14px;color:var(--orange);padding:12px 0 0 14px;font-weight:500}
.card h5{font-size:30px;color:#fff;font-weight:700;padding-left:14px;line-height:34px;letter-spacing:2px}
.card .more{position:absolute;right:24px;bottom:18px;color:#fff;font-size:14px;font-weight:600;display:flex;align-items:center;gap:8px}
.footer{left:0;top:4715px;width:1200px;height:268px;background:var(--navy)}
.cta{left:162px;top:4668px;width:878px;height:92px;background:var(--orange)}
.cta h6{position:absolute;left:16px;top:18px;font-size:25px;color:#fff;font-weight:700;letter-spacing:1px}
.cta p{position:absolute;left:16px;top:58px;font-size:14px;color:#fff;font-weight:500}
.cta .big{position:absolute;left:634px;top:6px;font-family:"Krona One",sans-serif;font-size:60px;color:transparent;-webkit-text-stroke:2px #fff}
.cta .learn{position:absolute;left:790px;top:38px;width:74px;height:26px;background:#fff;color:var(--navy);font-size:15px;font-weight:700;display:flex;align-items:center;justify-content:center}
.foot-brand{left:0;top:4790px;width:1200px;justify-content:center;color:#fff;font-size:34px}
.foot-nav{left:0;top:4870px;width:1200px;display:flex;justify-content:center;gap:64px;color:#fff;font-size:25px;font-weight:500}
.foot-rule{left:0;top:4922px;width:1200px;height:1px;background:#5a72a3}
.socials{left:0;top:4938px;width:1200px;display:flex;justify-content:center;gap:49px}
.socials i{width:38px;height:38px;border-radius:50%;background:#fff;display:block}
</style>
</head>
<body>

<header>
  <div class="abs brand" style="left:46px;top:26px;font-size:28px"><span class="brand-dot"></span>Driftwell Solar</div>
  <nav class="nav"><span>About</span><span>Team</span><span>Solutions</span><span>Projects</span><span>News Update</span><span>Contact</span></nav>
</header>

<section class="hero">
  <div class="abs hero-bg" role="img" aria-label="Solar panel field with a woman walking between the rows"></div>
  <div class="abs hero-bg-low" role="img" aria-label="Grass beneath the solar field"></div>
  <div class="abs display hero-solar">SOLAR</div>
  <div class="abs display hero-energy">ENERGY</div>
  <h1 class="abs hero-title">Investing in Clean<br>Energy Generation</h1>
  <p class="abs hero-copy">Our investment in emissions-free and clean generation has reduced our impact on the air we breathe and demonstrate our commitment.</p>
  <a class="btn btn-solutions">Solutions</a>
  <a class="btn btn-projects">Projects</a>
  <div class="abs stats-photo" role="img" aria-label="Engineer standing beside a solar array"></div>
  <div class="abs stats">
    <div class="stat">
      <svg width="70" height="62" viewBox="0 0 70 62" fill="none" stroke="#fff" stroke-width="2"><path d="M8 50 L22 18 L52 18 L40 50 Z"/><path d="M15 34 H46 M30 18 L24 50 M41 18 L33 50"/><path d="M30 50 V58 M22 58 H38"/><circle cx="58" cy="10" r="5"/><path d="M58 1v3 M58 16v3 M49 10h3 M64 10h3"/></svg>
      <div class="stat-num">18000+</div><div class="stat-label">units installed</div>
    </div>
    <div class="stat">
      <svg width="70" height="62" viewBox="0 0 70 62" fill="none" stroke="#fff" stroke-width="2"><path d="M35 4 L22 58 M35 4 L48 58 M26 40 H44 M29 26 H41 M18 18 H52 M22 30 H48 M24 40 L46 58 M46 40 L24 58"/></svg>
      <div class="stat-num">12 MW+</div><div class="stat-label">production</div>
    </div>
    <div class="stat">
      <svg width="70" height="62" viewBox="0 0 70 62" fill="none" stroke="#fff" stroke-width="2.5"><circle cx="35" cy="18" r="13"/><path d="M10 60 V50 Q10 36 24 36 H46 Q60 36 60 50 V60 Z"/></svg>
      <div class="stat-num">2500+</div><div class="stat-label">Customers</div>
    </div>
  </div>
</section>

<section class="about">
  <div class="abs about-photo" role="img" aria-label="Two engineers in hard hats reviewing plans at a solar site"></div>
  <div class="abs about-badge"><b>10+</b><span>YEARS<br>EXPERINCED</span></div>
  <div class="abs outline-title about-title">ABOUT</div>
  <div class="abs sub-blue" style="left:603px;top:1107px">Who we are?</div>
  <ul class="abs about-list">
    <li>Established in 2019.</li>
    <li>Subsidiary of Harlow Brenwick Infrastructure Ltd &amp; Tamsel Profiles Pvt. Ltd.</li>
    <li>Harlow Brenwick Infrastructure Ltd.</li>
    <li class="sub">3 Decades of experience in plastic.</li>
    <li class="sub">A leading supplier in North India for Water Storage Tanks, Road Safety equipment and Solid Waste Management products.</li>
    <li>Tamsel Profiles Pvt. Ltd.</li>
    <li class="sub">Leading supplier of module mounting structures in India with an annual supply of more than 5GW.</li>
  </ul>
  <a class="abs find-more"><svg width="24" height="24" viewBox="0 0 24 24" fill="none" stroke="#fff" stroke-width="2"><circle cx="12" cy="12" r="10"/><path d="M12 7v10M7 12h10"/></svg>Find More</a>
</section>

<section class="abs partners">
  <div class="partner"><i></i>Kessolt</div>
  <div class="partner"><i></i>Varentis</div>
  <div class="partner">Pellagro</div>
  <div class="partner">Norvane</div>
</section>

<section class="team-section">
  <div class="abs team" role="img" aria-label="Team working together around a table, tinted blue"></div>
  <h2 class="abs team-title">TEAM MEMBERS</h2>
  <div class="member" style="left:99px"><div class="portrait" style="background:linear-gradient(#c9b6a6,#7a5d4d)" role="img" aria-label="Portrait of Owen Hartley"></div><div class="name">OWEN HARTLEY</div><div class="role">Electrical Engineer</div></div>
  <div class="member" style="left:464px"><div class="portrait" style="background:linear-gradient(#e4d5c8,#a8704a)" role="img" aria-label="Portrait of Clara Denn"></div><div class="name">CLARA DENN</div><div class="role">Technician</div></div>
  <div class="member" style="left:841px"><div class="portrait" style="background:linear-gradient(#d9d9d9,#3b2e2a)" role="img" aria-label="Portrait of Mrs. Varga"></div><div class="name">MRS. VARGA</div><div class="role">Accountant</div></div>
</section>

<section class="estimate">
  <div class="abs est-form"></div>
  <div class="abs est-photo" role="img" aria-label="Large floating solar installation on a reservoir"><h3>COMMERCIAL</h3><h4>PROJECTS</h4></div>
  <h2 class="abs est-title">FIND AN<br>ESTIMATION</h2>
  <div class="field" style="top:2505px">NAME</div>
  <div class="field" style="top:2557px">EMAIL</div>
  <div class="field" style="top:2608px">POWER REQUIRED</div>
  <div class="field" style="top:2660px">BUDGET</div>
  <div class="field" style="top:2711px">LOCATION</div>
  <a class="abs calc">CALCULATE</a>
</section>

<section class="facts">
  <div class="abs outline-title facts-title">FACTS</div>
  <h2 class="abs facts-sub">Greener Tomorrow<br>for Everyone</h2>
  <p class="abs facts-copy">Sustainable development is the creed that underpins Driftwell's bespoke initiatives to protect the environment, strengthen communities and propel responsible growth.</p>
  <div class="abs map" role="img" aria-label="Outline map of India marking project sites"></div>
  <svg class="abs" style="left:848px;top:3010px" width="40" height="52" viewBox="0 0 40 52"><path d="M20 50 L6 28 A16 16 0 1 1 34 28 Z" fill="var(--orange)" stroke="#23417f" stroke-width="3"/><circle cx="20" cy="18" r="7" fill="var(--blue)"/></svg>
  <svg class="abs" style="left:773px;top:3170px" width="40" height="52" viewBox="0 0 40 52"><path d="M20 50 L6 28 A16 16 0 1 1 34 28 Z" fill="var(--orange)" stroke="#23417f" stroke-width="3"/><circle cx="20" cy="18" r="7" fill="var(--blue)"/></svg>
  <svg class="abs" style="left:896px;top:3265px" width="40" height="52" viewBox="0 0 40 52"><path d="M20 50 L6 28 A16 16 0 1 1 34 28 Z" fill="var(--orange)" stroke="#23417f" stroke-width="3"/><circle cx="20" cy="18" r="7" fill="var(--blue)"/></svg>
  <div class="map-label" style="left:898px;top:3032px">Sonipat, Haryana</div>
  <div class="map-label" style="left:650px;top:3110px">Sanand,<br>Ahmedabad</div>
  <div class="map-label" style="left:924px;top:3312px">Ramagundam,<br>Telengana</div>
</section>

<section class="work">
  <div class="abs work-bg"></div>
  <div class="abs display work-ghost">WORK</div>
  <h2 class="abs work-title">OUR RECENT PROJECTS</h2>
  <p class="abs work-copy">All functions including supply chain, value chain, project scheduling, manufacturing, services and spares, technology, R&amp;D, etc. are integrated to give a complete solutions package.</p>
  <div class="proj" style="left:18px;background:linear-gradient(180deg,#e9eef2,#8a97a6 55%,#4f6a8c)" role="img" aria-label="Solar plant beside an industrial site"></div>
  <div class="proj" style="left:258px;background:linear-gradient(135deg,#2f5a98,#0f2c5a 50%,#2f6d8a)" role="img" aria-label="Floating solar rows on dark water"></div>
  <div class="proj" style="left:500px;background:linear-gradient(180deg,#f2bb45,#e8a92a)" role="img" aria-label="Solar field under golden light"></div>
  <div class="proj" style="left:742px;background:linear-gradient(135deg,#6d8fc4,#3e63a4)" role="img" aria-label="Close view of a solar array"></div>
  <div class="proj" style="left:983px;background:linear-gradient(135deg,#5aaee0,#2a7cc4 60%,#7fb7a5)" role="img" aria-label="Aerial view of a floating solar plant"></div>
  <div class="abs query"></div>
  <div class="abs query-photo" role="img" aria-label="Solar panels tinted blue"></div>
  <div class="abs query-label">ASK US ANY<br>QUERY</div>
  <div class="qfield" style="left:494px;width:164px">NAME</div>
  <div class="qfield" style="left:673px;width:164px">EMAIL</div>
  <div class="abs send">SEND</div>
</section>

<section class="blogs">
  <div class="abs outline-title blogs-ghost">BLOGS</div>
  <h2 class="abs blogs-title">News Updates</h2>
  <svg class="abs plus" viewBox="0 0 92 92"><path d="M46 24v44M24 46h44" stroke="#fff" stroke-width="7" stroke-linecap="round"/></svg>
  <article class="card" style="left:132px"><div class="img" style="background:linear-gradient(180deg,#c5d6e6,#6f7f92 60%,#8a9a70)" role="img" aria-label="House roof covered with solar panels"></div><div class="date">DECEMBER 20,2021</div><h5>HELPING TO<br>GO GREEN</h5><div class="more">READ MORE <svg width="12" height="14"><path d="M0 0L12 7L0 14Z" fill="#fff"/></svg></div></article>
  <article class="card" style="left:465px"><div class="img" style="background:linear-gradient(180deg,#dfe6ec,#7b8fa8 50%,#7f9367)" role="img" aria-label="Family walking past solar panels"></div><div class="date">JANUARY 25,2022</div><h5>ENERGY<br>TRANSITION</h5><div class="more">READ MORE <svg width="12" height="14"><path d="M0 0L12 7L0 14Z" fill="#fff"/></svg></div></article>
  <article class="card" style="left:798px"><div class="img" style="background:linear-gradient(180deg,#4f6fa3,#c89a7a 70%,#5d6c86)" role="img" aria-label="City skyline with a ferris wheel at dusk"></div><div class="date">MARCH 15,2022</div><h5>POLLUTION<br>PROBLEMS</h5><div class="more">READ MORE <svg width="12" height="14"><path d="M0 0L12 7L0 14Z" fill="#fff"/></svg></div></article>
</section>

<footer>
  <div class="abs footer"></div>
  <div class="abs cta">
    <h6>Have Questions? We are Here to Help You!</h6>
    <p>DRIFTWELL is among the India's leading renewable energy solutions provider.</p>
    <div class="big">24/7</div>
    <a class="learn">LEARN</a>
  </div>
  <div class="abs brand foot-brand"><span class="brand-dot"></span>Driftwell Solar</div>
  <nav class="abs foot-nav"><span>About</span><span>Team</span><span>Solutions</span><span>Projects</span><span>News Update</span><span>Contact</span></nav>
  <div class="abs foot-rule"></div>
  <div class="abs socials"><i></i><i></i><i></i><i></i><i></i></div>
</footer>

</body>
</html>
```